Project Planning & Communication Process

Need a PowerPoint slide that illustrates our project planning and communication cycle. Our company has key meetings, and key communication vehicles (like emails and follow up tools) that we use to ensure our frontline staff are prepared to execute the new project successfully. This document needs to call out how the different components, like the meetings and emails, work together (like a flow chart), so someone who needs to use this process will understand what they should do. The slide needs to be simple yet comprehensive enough to guide someone through the details. I don't want it overwhelming. The primary focus is the process, not the details.

Use the color pallette included within the slide (shades of blue and gray, and black). This is for an insurance company (www.harborquill.com). Use this as a reference for the look and feel.

I have attached a sample slide of the flow chart process.

Click here if you cannot access the file. https://www.filecrate.example/s/q8wz2mbt7ypnc4r/Communcation_Methods_V1.pptx

If you are not able to see the uploaded slide.  Please send me your email address and I will send the slide to you directly. 

ISince I'm not able to upload the reference ppt file, 've uploaded the slide at FileCrate.  Please click here to access.
https://www.filecrate.example/s/q8wz2mbt7ypnc4r/Communcation_Methods_V1.pptx

Reason: extending one more day for designers to make last minute updates.

Target Market(s)

Vice Presidents and project managers/business partners within the organization.

Industry/Entity Type

Communication

Font styles to use
Sans Serif

Colors
3176b5

Requirements
Must have
• 1 page, color pallette assigned, be simple yet comprehensive. the focus needs to be on the process, not on the details.
Nice to have
• Doesn't have to follow the example I provided. Please feel free to approach from different ways.

```html
<!DOCTYPE html>
<html lang="en">
<head>
<meta charset="utf-8">
<title>Project Planning and Communication Cycle</title>
<link href="https://fonts.googleapis.com/css2?family=Signika:wght@400;600;700&family=Open+Sans:ital,wght@0,400;0,600;1,400&display=swap" rel="stylesheet">
<style>
  :root {
    --page-bg: #eef0f2;
    --slide-bg: #ffffff;
    --ink-dark: #333333;
    --ink-gray: #6e6e6e;
    --brand-blue: #3176b5;
    --sky-blue: #a9c3de;
    --floor-light: #f6f6f6;
    --floor-mid: #c9c9c9;
    --floor-dark: #3c3c3c;
    --line-gray: #a8a8a8;
    --box-orange: #e98a25;
    --box-amber: #f2a23a;
    --box-lime: #cfdc1e;
    --box-yellow: #f3e23e;
    --box-sage: #e3ebe0;
    --arrow-down: #a23fc2;
    --arrow-up: #f3a41d;
    --arrow-side: #e23434;
    --black: #111111;
    --white: #ffffff;
  }
  * { box-sizing: border-box; margin: 0; padding: 0; }
  html, body {
    width: 1200px; height: 1000px; overflow: hidden;
    background: var(--page-bg);
    font-family: "Open Sans", Arial, sans-serif;
  }
  .deck {
    width: 1200px; height: 1000px;
    display: flex; flex-direction: column; align-items: center; justify-content: center;
    gap: 28px;
  }
  .slide {
    position: relative; width: 620px; height: 465px; overflow: hidden;
    background: var(--slide-bg);
    box-shadow: 0 4px 18px rgba(0,0,0,.18);
  }
  .floor {
    position: absolute; left: 0; right: 0; bottom: 0;
  }
  .brand {
    position: absolute; display: flex; align-items: center; gap: 8px;
    font-family: "Signika", Arial, sans-serif; font-weight: 700;
    line-height: .95; letter-spacing: .5px;
  }
  .brand__mark { flex: none; background: var(--brand-blue); }

  /* title slide */
  .title-slide .floor {
    height: 140px;
    background: linear-gradient(to bottom, var(--floor-light), var(--floor-mid));
  }
  .title-slide__heading {
    position: absolute; left: 30px; top: 32px;
    font-family: "Signika", Arial, sans-serif; font-weight: 700;
    font-size: 18px; letter-spacing: .4px; color: var(--ink-dark);
  }
  .title-slide__people {
    position: absolute; left: 40px; bottom: 0; width: 290px; height: 330px;
    background: linear-gradient(to bottom, rgba(169,195,222,.25) 0%, rgba(169,195,222,.5) 40%, var(--brand-blue) 100%);
  }
  .title-slide__subtitle {
    position: absolute; right: 36px; top: 140px; text-align: right;
    font-size: 13px; line-height: 1.3; color: var(--ink-dark);
  }
  .title-slide .brand { left: 380px; top: 210px; font-size: 22px; color: var(--ink-gray); }
  .title-slide .brand .brand__mark { width: 26px; height: 26px; }

  /* section slide */
  .section-slide .floor {
    height: 120px;
    background: linear-gradient(to bottom, var(--floor-light), var(--floor-dark));
  }
  .section-slide__corner { position: absolute; left: 0; top: 0; width: 26px; height: 42px; background: var(--brand-blue); }
  .section-slide__label {
    position: absolute; left: 36px; top: 12px;
    font-family: "Signika", Arial, sans-serif; font-weight: 700; font-style: italic;
    font-size: 22px; color: var(--brand-blue);
  }
  .section-slide__square { position: absolute; left: 8px; top: 42px; width: 22px; height: 22px; background: var(--black); }
  .section-slide__sub {
    position: absolute; left: 38px; top: 42px;
    font-size: 15px; line-height: 22px; color: var(--ink-dark);
  }
  .section-slide .brand { right: 22px; top: 16px; font-size: 14px; color: var(--brand-blue); }
  .section-slide .brand .brand__mark { width: 16px; height: 16px; }
  .section-slide__chart { position: absolute; left: 0; top: 0; }
  .section-slide__caption {
    position: absolute; left: 0; right: 0; bottom: 26px; text-align: center;
    font-style: italic; font-size: 15px; color: var(--white);
  }
  .chart-box rect { stroke: var(--white); stroke-width: 2; filter: drop-shadow(0 1px 2px rgba(0,0,0,.25)); }
  .chart-box text { font-family: "Open Sans", Arial, sans-serif; font-size: 9px; fill: #333; }
  .legend text { font-family: "Open Sans", Arial, sans-serif; font-size: 8px; fill: #333; }
</style>
</head>
<body>
<main class="deck">

  <section class="slide title-slide">
    <div class="floor"></div>
    <h1 class="title-slide__heading">PROJECT PLANNING AND COMMUNICATION CYCLE</h1>
    <div class="title-slide__people" role="img" aria-label="Blue silhouettes of a team of business people standing together"></div>
    <p class="title-slide__subtitle">Key meetings and<br>Key communication vehicle</p>
    <div class="brand"><span class="brand__mark"></span><span>COMPANY<br>LOGO</span></div>
  </section>

  <section class="slide section-slide">
    <div class="floor"></div>
    <div class="section-slide__corner"></div>
    <div class="section-slide__label">SECTION 1</div>
    <div class="section-slide__square"></div>
    <div class="section-slide__sub">Company Communication</div>
    <div class="brand"><span class="brand__mark"></span><span>COMPANY<br>LOGO</span></div>

    <svg class="section-slide__chart" width="620" height="465" viewBox="0 0 620 465">
      <defs>
        <marker id="head-down" markerWidth="6" markerHeight="6" refX="5" refY="3" orient="auto"><path d="M0,0 L6,3 L0,6z" fill="#a23fc2"/></marker>
        <marker id="head-up" markerWidth="6" markerHeight="6" refX="5" refY="3" orient="auto"><path d="M0,0 L6,3 L0,6z" fill="#f3a41d"/></marker>
        <marker id="head-side" markerWidth="6" markerHeight="6" refX="5" refY="3" orient="auto-start-reverse"><path d="M0,0 L6,3 L0,6z" fill="#e23434"/></marker>
      </defs>

      <g stroke="var(--line-gray)" stroke-width="1.5" fill="none">
        <path d="M300 112 V124 H96 V170 M175 124 V168 M300 124 H510 V102 M390 124 V132"/>
        <path d="M175 210 V224 H140 V240 M175 224 H235 V228"/>
        <path d="M235 270 V296"/>
        <path d="M390 172 V190 H320 V212 M390 190 H450 V204"/>
        <path d="M320 254 V284 M450 246 V280"/>
      </g>

      <g class="chart-box">
        <rect x="260" y="78" width="80" height="34" rx="4" fill="var(--box-orange)"/><text x="300" y="98" text-anchor="middle">Owner-President</text>
        <rect x="352" y="132" width="76" height="40" rx="4" fill="var(--box-sage)"/><text x="390" y="149" text-anchor="middle">Operations</text><text x="390" y="161" text-anchor="middle">Manager</text>
        <rect x="472" y="62" width="76" height="40" rx="4" fill="var(--box-yellow)"/><text x="510" y="80" text-anchor="middle">H.R.</text><text x="510" y="92" text-anchor="middle">Manager</text>
        <rect x="62" y="170" width="66" height="38" rx="4" fill="var(--box-amber)"/><text x="95" y="186" text-anchor="middle">Accounting</text><text x="95" y="198" text-anchor="middle">Manager</text>
        <rect x="142" y="168" width="66" height="42" rx="4" fill="var(--box-lime)"/><text x="175" y="186" text-anchor="middle">Marketing</text><text x="175" y="198" text-anchor="middle">Manager</text>
        <rect x="106" y="240" width="68" height="40" rx="4" fill="var(--box-lime)"/><text x="140" y="257" text-anchor="middle">Advertising</text><text x="140" y="269" text-anchor="middle">Supervisor</text>
        <rect x="202" y="228" width="66" height="42" rx="4" fill="var(--box-lime)"/><text x="235" y="246" text-anchor="middle">Sales</text><text x="235" y="258" text-anchor="middle">Supervisor</text>
        <rect x="206" y="296" width="58" height="40" rx="4" fill="var(--box-lime)"/><text x="235" y="313" text-anchor="middle">Sales</text><text x="235" y="325" text-anchor="middle">Staff</text>
        <rect x="282" y="212" width="76" height="42" rx="4" fill="var(--box-sage)"/><text x="320" y="230" text-anchor="middle">Note-Takers</text><text x="320" y="242" text-anchor="middle">Supervisor</text>
        <rect x="414" y="204" width="72" height="42" rx="4" fill="var(--box-sage)"/><text x="450" y="222" text-anchor="middle">Copiers</text><text x="450" y="234" text-anchor="middle">Supervisor</text>
        <rect x="286" y="284" width="68" height="36" rx="4" fill="var(--box-sage)"/><text x="320" y="305" text-anchor="middle">Note-Takers</text>
        <rect x="416" y="280" width="70" height="40" rx="4" fill="var(--box-sage)"/><text x="451" y="303" text-anchor="middle">Copiers</text>
      </g>

      <g fill="none" stroke-width="1.8">
        <path d="M285 112 C250 150 220 170 210 180" stroke="var(--arrow-down)" marker-end="url(#head-down)"/>
        <path d="M190 210 C195 240 182 255 176 258" stroke="var(--arrow-down)" marker-end="url(#head-down)"/>
        <path d="M345 240 C372 255 366 285 356 298" stroke="var(--arrow-down)" marker-end="url(#head-down)"/>
        <path d="M380 132 C360 120 345 118 332 112" stroke="var(--arrow-up)" marker-end="url(#head-up)"/>
        <path d="M300 212 C285 175 325 150 350 150" stroke="var(--arrow-up)" marker-end="url(#head-up)"/>
        <path d="M210 310 C190 290 194 262 200 250" stroke="var(--arrow-up)" marker-end="url(#head-up)"/>
        <path d="M108 170 C115 160 130 158 140 176" stroke="var(--arrow-side)" marker-start="url(#head-side)" marker-end="url(#head-side)"/>
        <path d="M360 222 C385 200 400 206 412 214" stroke="var(--arrow-side)" marker-start="url(#head-side)" marker-end="url(#head-side)"/>
        <path d="M266 330 C330 352 410 345 440 322" stroke="var(--arrow-side)" marker-start="url(#head-side)" marker-end="url(#head-side)"/>
      </g>

      <g class="legend">
        <rect x="80" y="362" width="460" height="18" fill="#ffffff" stroke="#cccccc"/>
        <line x1="92" y1="376" x2="108" y2="368" stroke="#a23fc2" stroke-width="1.8" marker-end="url(#head-down)"/><text x="114" y="374">Downward communication</text>
        <line x1="232" y1="376" x2="248" y2="368" stroke="#f3a41d" stroke-width="1.8" marker-end="url(#head-up)"/><text x="254" y="374">Upward communication</text>
        <line x1="372" y1="376" x2="388" y2="368" stroke="#e23434" stroke-width="1.8" marker-end="url(#head-side)"/><text x="394" y="374">Horizontal communication</text>
      </g>
    </svg>

    <p class="section-slide__caption">Company communication chart</p>
  </section>

</main>
</body>
</html>
```